ZOVA Framework. the way you communicate in every situation and in all environments.

I would like you to create a diagram depicting a very specific process of communication. it must follow the look of the diagram that i have attached. this is going to be used in a book called BEDROCK. it is going to explain the fact that we communicate all the same way using this process as we communicate. it starts with the fact that everyone takes everything that is said personally and then moves on to filters, which is your own agenda or experience kicking in. then you move to your why it matters, which is your motivation and ends with the choice of words you use when you communicate. if you are going to be successful then you must separate the person from the issue.

Target Market(s)

market is executive business people around the world

Industry/Entity Type

Consulting

Font styles to use
Sans Serif

Colors

Designer to choose only greyscale colors for use in the design.

Requirements
Must have
• I would like it to have a diving/ocean/snorkel feel to it. The analogy we are using is to make a deep dive when you are communicating. it must have every part of the diagram you see, it starts at the top with the zova framework (and the words) it then connects to the filters which connects to the why it matters with connects to the words and then end with the separating the person from the issue.
Nice to have
• we are writing a black and white book NO color. therefore the words should be clear and easy to read. Each section should be able to stand on its own so we can write about it separately.
Should not have
• the diagram DOES NOT have to look like the one i gave you. it must explain the fact that it starts with ZOVA and ends with Separate and must pass through the three areas to get to the SEPARATE.

```html
<!DOCTYPE html>
<html lang="en">
<head>
<meta charset="utf-8">
<title>ZOVA Framework – BEDROCK</title>
<link rel="stylesheet" href="https://fonts.googleapis.com/css2?family=Montserrat:wght@700;800&family=Roboto:wght@400;700&display=swap">
<style>
  :root {
    --ink: #000000;
    --paper: #ffffff;
    --band: #6d6e71;
    --heading-font: "Montserrat", Arial, sans-serif;
    --body-font: "Roboto", Arial, sans-serif;
  }
  html, body {
    margin: 0;
    padding: 0;
    width: 927px;
    height: 1200px;
    overflow: hidden;
    background: var(--paper);
  }
  .page {
    position: relative;
    width: 927px;
    height: 1200px;
    background: var(--paper);
    font-family: var(--body-font);
    color: var(--ink);
  }
  .diagram-frame {
    position: absolute;
    left: 68px;
    top: 97px;
    width: 787px;
    height: 955px;
    border: 2px solid var(--ink);
  }
  .stage {
    position: absolute;
  }
  .stage svg {
    display: block;
    width: 100%;
    height: 100%;
    overflow: visible;
  }
  .stage-ring { fill: var(--ink); }
  .stage-core { fill: var(--paper); }
  .stage-band { fill: var(--band); }
  .stage-title {
    font-family: var(--heading-font);
    font-weight: 800;
    font-size: 23px;
    letter-spacing: 0.5px;
    fill: var(--paper);
    text-transform: uppercase;
  }
  .stage-copy {
    position: absolute;
    left: 0;
    width: 100%;
    text-align: center;
    line-height: 1.25;
    margin: 0;
  }
  .stage-copy strong { font-weight: 700; }
  .stage-copy--large { font-size: 13px; line-height: 1.3; }
  .stage-copy--small { font-size: 11px; line-height: 1.2; }

  .flow-arrow {
    position: absolute;
    width: 38px;
    height: 18px;
  }
  .flow-arrow polyline {
    fill: none;
    stroke: var(--ink);
    stroke-width: 3;
    stroke-linecap: square;
  }

  .book-band {
    position: absolute;
    left: 68px;
    top: 1092px;
    width: 791px;
    height: 38px;
    border-radius: 19px;
    background: var(--ink);
    color: var(--paper);
    font-family: var(--heading-font);
    font-weight: 700;
    font-size: 22px;
    letter-spacing: 14px;
    text-align: center;
    line-height: 38px;
    text-indent: 14px;
  }
</style>
</head>
<body>
<main class="page">
  <div class="diagram-frame"></div>

  <!-- Stage 1: ZOVA Framework -->
  <section class="stage" style="left:353px;top:205px;width:220px;height:220px;">
    <svg viewBox="-110 -110 220 220" aria-hidden="true">
      <defs>
        <clipPath id="band-clip-1"><rect x="-110" y="-7" width="220" height="120"/></clipPath>
        <path id="arc-1" d="M -96 0 A 96 96 0 0 1 96 0"/>
      </defs>
      <circle class="stage-ring" r="108"/>
      <circle class="stage-core" r="84"/>
      <circle class="stage-band" r="84" clip-path="url(#band-clip-1)"/>
      <circle class="stage-core" cy="-15" r="72"/>
      <text class="stage-title" dy="8"><textPath href="#arc-1" startOffset="50%" text-anchor="middle">ZOVA Framework</textPath></text>
    </svg>
    <p class="stage-copy stage-copy--large" style="top:50px;">When<br>words are<br>taken<br>personally,<br><strong>What<br>happens?</strong></p>
  </section>

  <svg class="flow-arrow" style="left:304px;top:364px;transform:rotate(-15deg);" viewBox="0 0 38 18" aria-hidden="true">
    <polyline points="10,2 3,9 10,16"/><polyline points="21,2 14,9 21,16"/><polyline points="32,2 25,9 32,16"/>
  </svg>

  <!-- Stage 2: Your Filters -->
  <section class="stage" style="left:131px;top:358px;width:167px;height:167px;">
    <svg viewBox="-110 -110 220 220" aria-hidden="true">
      <defs>
        <clipPath id="band-clip-2"><rect x="-110" y="-7" width="220" height="120"/></clipPath>
        <path id="arc-2" d="M -96 0 A 96 96 0 0 1 96 0"/>
      </defs>
      <circle class="stage-ring" r="108"/>
      <circle class="stage-core" r="84"/>
      <circle class="stage-band" r="84" clip-path="url(#band-clip-2)"/>
      <circle class="stage-core" cy="-15" r="72"/>
      <text class="stage-title" dy="8"><textPath href="#arc-2" startOffset="50%" text-anchor="middle">Your Filters</textPath></text>
    </svg>
    <p class="stage-copy stage-copy--small" style="top:44px;">An<br>accumulation<br>of your<br><strong>experience,<br>knowledge and<br>value</strong></p>
  </section>

  <svg class="flow-arrow" style="left:320px;top:488px;transform:rotate(15deg);" viewBox="0 0 38 18" aria-hidden="true">
    <polyline points="5,2 12,9 5,16"/><polyline points="16,2 23,9 16,16"/><polyline points="27,2 34,9 27,16"/>
  </svg>

  <!-- Stage 3: Why It Matters -->
  <section class="stage" style="left:372px;top:480px;width:183px;height:183px;">
    <svg viewBox="-110 -110 220 220" aria-hidden="true">
      <defs>
        <clipPath id="band-clip-3"><rect x="-110" y="-7" width="220" height="120"/></clipPath>
        <path id="arc-3" d="M -96 0 A 96 96 0 0 1 96 0"/>
      </defs>
      <circle class="stage-ring" r="108"/>
      <circle class="stage-core" r="84"/>
      <circle class="stage-band" r="84" clip-path="url(#band-clip-3)"/>
      <circle class="stage-core" cy="-15" r="72"/>
      <text class="stage-title" dy="8"><textPath href="#arc-3" startOffset="50%" text-anchor="middle">Why It Matters</textPath></text>
    </svg>
    <p class="stage-copy stage-copy--small" style="top:68px;">This is your<br>compass, It is <strong>What<br>motivates you,<br>What drives you.</strong></p>
  </section>

  <svg class="flow-arrow" style="left:566px;top:640px;transform:rotate(15deg);" viewBox="0 0 38 18" aria-hidden="true">
    <polyline points="5,2 12,9 5,16"/><polyline points="16,2 23,9 16,16"/><polyline points="27,2 34,9 27,16"/>
  </svg>

  <!-- Stage 4: Your Words -->
  <section class="stage" style="left:632px;top:629px;width:167px;height:167px;">
    <svg viewBox="-110 -110 220 220" aria-hidden="true">
      <defs>
        <clipPath id="band-clip-4"><rect x="-110" y="-7" width="220" height="120"/></clipPath>
        <path id="arc-4" d="M -96 0 A 96 96 0 0 1 96 0"/>
      </defs>
      <circle class="stage-ring" r="108"/>
      <circle class="stage-core" r="84"/>
      <circle class="stage-band" r="84" clip-path="url(#band-clip-4)"/>
      <circle class="stage-core" cy="-15" r="72"/>
      <text class="stage-title" dy="8"><textPath href="#arc-4" startOffset="50%" text-anchor="middle">Your Words</textPath></text>
    </svg>
    <p class="stage-copy stage-copy--small" style="top:44px;">This is<br>your immediate<br>response,<br><strong>verbal or perhaps<br>non-verbal.</strong></p>
  </section>

  <svg class="flow-arrow" style="left:582px;top:764px;transform:rotate(-15deg);" viewBox="0 0 38 18" aria-hidden="true">
    <polyline points="10,2 3,9 10,16"/><polyline points="21,2 14,9 21,16"/><polyline points="32,2 25,9 32,16"/>
  </svg>

  <!-- Stage 5: What To Do -->
  <section class="stage" style="left:353px;top:740px;width:220px;height:220px;">
    <svg viewBox="-110 -110 220 220" aria-hidden="true">
      <defs>
        <clipPath id="band-clip-5"><rect x="-110" y="-7" width="220" height="120"/></clipPath>
        <path id="arc-5" d="M -96 0 A 96 96 0 0 1 96 0"/>
      </defs>
      <circle class="stage-ring" r="108"/>
      <circle class="stage-core" r="84"/>
      <circle class="stage-band" r="84" clip-path="url(#band-clip-5)"/>
      <circle class="stage-core" cy="-15" r="72"/>
      <text class="stage-title" dy="8"><textPath href="#arc-5" startOffset="50%" text-anchor="middle">What To Do</textPath></text>
    </svg>
    <p class="stage-copy stage-copy--large" style="top:90px;"><strong>Separate the<br>person from<br>the issue</strong></p>
  </section>

  <div class="book-band">BEDROCK</div>
</main>
</body>
</html>
```